VantoMedix website

I have a plumfield hosting website already & have been using wordpress.
See www.vantomedix-sample.com
I have a logo's already.
I need a front page "VantoMedix". I have 3 products: (need separate pages)
1) the "GlideTray" (can't supply images ATM)
2) the "TubeKeeper" (several stills below & animation: http://www.clipvault-example.com/watch?v=Z7HqR20mW3x&list=QPtr8B_kzoepWnXcM4Lq5B_T&feature=share)
3) the "FastPart" animation here: http://clipv.example/pwrtk-Mmo_E & logo as below

It needs to be corporate & professional looking. VantoMedix is an innovative design house for medical devices.

Reason: Hi Designers, thanks for all your work to date - there have been some great designs. We'll be providing feedback to some of you in the near future. The reason we have extended the deadline is simply that we are too busy with other aspects of the business to focus on this at the moment. Kind regards, the VantoMedix team.

Dear Designers,

VantoMedix apologies for the delay due to our busyness. 
Please help us to understand the process here:
are we getting fully working websites? With multiple pages? Will we be able to modify them?
If not, what is the output?

Kind regards,
the Vanto team.

```html
<!DOCTYPE html>
<html lang="en">
<head>
<meta charset="utf-8">
<title>VantoMedix — Home</title>
<link rel="stylesheet" href="https://fonts.googleapis.com/css2?family=Open+Sans:wght@300;400;600;700&display=swap">
<style>
:root{
  --ink:#222831;
  --muted:#5b6169;
  --light-muted:#b3b8bd;
  --topbar:#1b1c1e;
  --page:#ffffff;
  --panel:#eceeef;
  --brand:#2a9fd8;
  --about:#3ea9df;
  --accent:#ff6a00;
  --accent-link:#f07a12;
  --navy:#283848;
  --footer:#1e1f21;
  --player:#1a1a1a;
  --progress:#d8261d;
}
*{box-sizing:border-box;margin:0;padding:0}
html,body{width:1200px;height:2545px;overflow:hidden}
body{background:var(--page);font-family:"Open Sans",Arial,sans-serif;color:var(--ink);position:relative}

/* top bar */
.topbar{position:absolute;top:0;left:0;width:1200px;height:34px;background:var(--topbar);color:#fff;font-size:11px}
.topbar .contact{position:absolute;left:94px;top:0;height:34px;display:flex;align-items:center;gap:10px}
.topbar .contact strong{font-weight:700;letter-spacing:.2px}
.topbar .contact span{display:flex;align-items:center;gap:6px}
.topbar .social{position:absolute;right:94px;top:5px;display:flex;gap:8px}
.topbar .social i{display:block;width:23px;height:23px;border:1.5px solid #cfd2d5;border-radius:50%}

/* header */
.site-header{position:absolute;top:34px;left:0;width:1200px;height:80px;background:#fff;box-shadow:0 1px 3px rgba(0,0,0,.12)}
.brand{position:absolute;left:94px;top:20px;font-weight:700;font-size:33px;color:var(--brand);letter-spacing:-.5px}
.main-nav{position:absolute;top:0;left:519px;height:80px;display:flex;align-items:center;font-size:12.5px;font-weight:700;color:#2b2f35}
.main-nav a{color:inherit;text-decoration:none;margin-right:30px}
.main-nav .shop{font-weight:400;margin-right:22px}
.main-nav .caret{font-size:9px;margin-left:6px;color:var(--brand)}
.main-nav svg{margin-right:22px}
.search-btn{position:absolute;left:1079px;top:26px;width:26px;height:26px;border-radius:50%;background:var(--brand);display:flex;align-items:center;justify-content:center}

/* hero */
.hero{position:absolute;top:114px;left:67px;width:1066px;height:649px;
  background:
    linear-gradient(180deg,rgba(120,140,110,.35) 0%,rgba(120,140,110,0) 30%),
    linear-gradient(90deg,#c9cccc 0%,#e6e7e6 25%,#d4d5d4 40%,#4a4d52 55%,#2a2c30 70%,#5a5d60 85%,#b8bbbb 100%)}

/* products */
.products{position:absolute;top:763px;left:67px;width:1066px;height:419px;background:var(--panel)}
.product{position:absolute;top:50px;width:321px;text-align:center}
.product .tag{font-size:11px;font-weight:700;letter-spacing:1px;color:var(--brand);height:16px}
.product h3{font-weight:400;font-size:20px;color:#333;margin-top:6px;letter-spacing:.5px}
.product .shot{display:block;width:321px;height:174px;margin-top:12px}
.product p{font-size:12px;line-height:20px;color:#3d4248;margin:20px auto 0;width:280px}
.product p a{color:var(--accent-link);font-weight:600;text-decoration:none}
.p1{left:25px}.p2{left:371px}.p3{left:720px}
.shot-glide{background:linear-gradient(180deg,#f4f5f7 0%,#b8c6d6 35%,#5c9fd0 55%,#c7d3df 80%,#f4f5f7 100%)}
.shot-tube{background:linear-gradient(160deg,#2a2b30 0%,#5e5f7a 40%,#9d9ec8 70%,#c9c9e0 100%)}
.shot-fast{background:linear-gradient(170deg,#ffffff 0%,#8a8b90 30%,#4a4b50 55%,#6d6e72 75%,#ffffff 100%)}

/* about */
.about{position:absolute;top:1182px;left:67px;width:1066px;height:325px;background:var(--about);color:#fff;text-align:center}
.section-title{font-weight:300;font-size:44px;line-height:1}
.about .section-title{margin-top:33px}
.section-sub{font-size:15px;margin-top:8px}
.about p{text-align:left;font-size:12px;line-height:18px;margin:40px 35px 0}

/* videos */
.videos{position:absolute;top:1507px;left:67px;width:1066px;height:464px;background:var(--panel);text-align:center}
.videos .cam{display:block;margin:55px auto 0}
.videos .section-title{margin-top:20px;color:#2a2e33}
.videos .section-sub{color:var(--light-muted);margin-top:10px}
.video{position:absolute;top:254px;width:321px;height:182px;background:var(--player);overflow:hidden;text-align:left}
.video .vt{position:absolute;left:10px;top:6px;color:#fff;font-size:11.5px;font-weight:600}
.video .frame{position:absolute;left:0;top:26px;width:321px;height:128px}
.video .play{position:absolute;left:136px;top:68px;width:50px;height:34px;border-radius:8px;background:rgba(20,20,20,.9);display:flex;align-items:center;justify-content:center}
.video .bar{position:absolute;left:0;bottom:0;width:321px;height:28px;background:#1b1b1b}
.video .track{position:absolute;left:0;bottom:28px;width:321px;height:3px;background:#555}
.video .track i{display:block;height:3px;background:var(--progress)}
.video .time{position:absolute;left:80px;bottom:8px;color:#ddd;font-size:10px}
.video .ctl{position:absolute;left:12px;bottom:9px}
.v1{left:25px}.v2{left:371px}.v3{left:720px}

/* gallery */
.gallery{position:absolute;top:1971px;left:67px;width:1066px;height:377px;background:var(--accent);color:#fff;text-align:center}
.gallery .section-title{margin-top:34px}
.gallery .section-sub{margin-top:10px}
.slide{position:absolute;top:139px;width:319px;height:172px}
.s1{left:35px;background:linear-gradient(160deg,#2b2d33,#7b7da0 55%,#c8c9dd)}
.s2{left:373px;background:linear-gradient(150deg,#a9a9cf,#d9dae8 60%,#9c9db8)}
.s3{left:712px;background:linear-gradient(170deg,#202225,#8e8fb5 55%,#d5d4e4)}
.arrow{position:absolute;top:214px}
.arrow.prev{left:52px}.arrow.next{right:52px}
.dots{position:absolute;top:325px;left:0;width:1066px;display:flex;justify-content:center;gap:5px}
.dots i{display:block;width:9px;height:9px;border:1.5px solid #fff;border-radius:50%}
.dots i.on{background:#fff}

/* newsletter */
.newsletter{position:absolute;top:2348px;left:67px;width:1066px;height:130px;background:#f1f2f3}
.newsletter h4{position:absolute;left:29px;top:40px;font-weight:400;font-size:22.5px;color:#2a2e33}
.newsletter p{position:absolute;left:29px;top:77px;font-size:11px;color:#2a2e33}
.field{position:absolute;top:49px;height:39px;background:#fff;border:1px solid #d6d9dc;font-size:11px;color:#a6abb0;padding:12px 8px}
.f1{left:418px;width:227px}.f2{left:661px;width:237px}
.subscribe{position:absolute;left:913px;top:49px;width:126px;height:39px;background:var(--navy);color:#fff;font-size:16px;display:flex;align-items:center;justify-content:center}

/* footer */
.site-footer{position:absolute;top:2478px;left:67px;width:1066px;height:67px;background:var(--footer);color:#8a8e93;font-size:11px}
.site-footer .copy{position:absolute;left:27px;top:27px}
.site-footer .copy a{color:var(--brand);text-decoration:none}
.site-footer .social{position:absolute;right:29px;top:14px;display:flex;gap:12px}
.site-footer .social i{display:block;width:38px;height:38px;border:1.5px solid #55585c;border-radius:50%}
</style>
</head>
<body>

<div class="topbar">
  <div class="contact">
    <strong>CALL US TODAY!</strong>
    <span><svg width="10" height="10" viewBox="0 0 10 10"><path d="M2 0.5l2 2-1 1.2c.6 1.3 1.5 2.2 2.8 2.8l1.2-1 2 2-1.3 1.5C4.5 8.8 1.2 5.5 .5 1.8z" fill="#fff"/></svg>+61 (0) 5550 10293</span>
    <span><svg width="11" height="8" viewBox="0 0 11 8"><rect width="11" height="8" fill="#fff"/><path d="M0 0l5.5 4.5L11 0" stroke="#1b1c1e" fill="none"/></svg>hello@vantomedix-sample.com</span>
  </div>
  <div class="social"><i></i><i></i><i></i><i></i></div>
</div>

<header class="site-header">
  <div class="brand">VantoMedix</div>
  <nav class="main-nav">
    <a href="#">HOME</a>
    <a href="#">ABOUT</a>
    <a href="#">PRODUCTS<span class="caret">▼</span></a>
    <a href="#">VIDEOS</a>
    <a href="#">CONTACT</a>
    <a href="#" class="shop">Shop</a>
    <svg width="13" height="12" viewBox="0 0 13 12"><path d="M0 1h2.5l1.8 7h7l1.4-5H3.5" fill="none" stroke="#2b2f35" stroke-width="1.6"/><circle cx="5" cy="10.5" r="1.2" fill="#2b2f35"/><circle cx="10" cy="10.5" r="1.2" fill="#2b2f35"/></svg>
    <svg width="11" height="12" viewBox="0 0 11 12"><circle cx="5.5" cy="3.2" r="3" fill="#2b2f35"/><path d="M0 12c0-4 2.5-5.5 5.5-5.5S11 8 11 12z" fill="#2b2f35"/></svg>
  </nav>
  <div class="search-btn"><svg width="12" height="12" viewBox="0 0 12 12"><circle cx="5" cy="5" r="3.6" fill="none" stroke="#fff" stroke-width="1.8"/><path d="M7.7 7.7L11 11" stroke="#fff" stroke-width="2"/></svg></div>
</header>

<section class="hero" role="img" aria-label="Photo: smiling paramedic in a dark uniform standing with arms crossed in front of a white ambulance"></section>

<section class="products">
  <article class="product p1">
    <div class="tag">GLIDETRAY</div>
    <h3>GLIDETRAY</h3>
    <div class="shot shot-glide" role="img" aria-label="Image: GlideTray product shown on a large display screen"></div>
    <p>Nullam vulputate euismod urna non pharetra. Phasellus euismod blandit mattis ipsum, ac laoreet lorem lacinia et. <a href="#">Read More.</a></p>
  </article>
  <article class="product p2">
    <div class="tag">TUBEKEEPER IV</div>
    <h3>TUBEKEEPER IV</h3>
    <div class="shot shot-tube" role="img" aria-label="Image: 3D render of the TubeKeeper device strapped to a forearm"></div>
    <p>Nullam vulputate euismod urna non pharetra. Phasellus euismod blandit mattis ipsum, ac laoreet lorem lacinia et. <a href="#">Read More.</a></p>
  </article>
  <article class="product p3">
    <div class="tag">FASTPART</div>
    <h3>FASTPART</h3>
    <div class="shot shot-fast" role="img" aria-label="Image: 3D render of the FastPart modular splint panels"></div>
    <p>Nullam vulputate euismod urna non pharetra. Phasellus euismod blandit mattis ipsum, ac laoreet lorem lacinia et. <a href="#">Read More.</a></p>
  </article>
</section>

<section class="about">
  <h2 class="section-title">About</h2>
  <div class="section-sub">Who we are and what we do</div>
  <p>Duis autem vel eum iriure dolor in hendrerit in vulputate velit esse molestie consequat, vel illum dolore eu feugiat nulla facilisis at vero eros et accumsan et iusto odio dignissim qui blandit praesent luptatum zzril delenit augue duis dolore te feugait nulla facilisi. Nam liber tempor cum soluta nobis eleifend option congue nihil imperdiet doming id quod mazim placerat facer possim assum. Typi non habent claritatem insitam; est usus legentis in iis qui facit eorum claritatem. Investigationes demonstraverunt lectores legere me lius quod ii legunt saepius. Claritas est etiam processus dynamicus, qui sequitur mutationem consuetudium lectorum. Mirum est notare quam littera gothica, quam nunc putamus parum claram, anteposuerit litterarum formas humanitatis per seacula quarta decima et quinta decima. Nam liber tempor cum soluta nobis eleifend option congue nihil imperdiet doming id quod mazim placerat facer possim assum. Typi non habent claritatem insitam.</p>
</section>

<section class="videos">
  <svg class="cam" width="90" height="66" viewBox="0 0 90 66"><circle cx="20" cy="15" r="14" fill="var(--brand)"/><circle cx="50" cy="15" r="14" fill="var(--brand)"/><rect x="4" y="28" width="62" height="36" rx="4" fill="var(--brand)"/><path d="M68 44l20-14v32z" fill="var(--brand)"/></svg>
  <h2 class="section-title">Featured Videos</h2>
  <div class="section-sub">Browse through our videos</div>

  <div class="video v1">
    <div class="vt">TUBEKEEPER</div>
    <div class="frame" role="img" aria-label="Video still: the TubeKeeper on a forearm" style="background:linear-gradient(90deg,#d9dbe6 0%,#9fa5d0 40%,#fff 70%,#fff 100%)"></div>
    <div class="play"><svg width="14" height="16"><path d="M0 0l14 8L0 16z" fill="#fff"/></svg></div>
    <div class="track"><i style="width:26%"></i></div>
    <div class="bar"><svg class="ctl" width="40" height="10"><path d="M0 0l8 5-8 5z" fill="#ddd"/><path d="M24 3h3l4-3v10l-4-3h-3z" fill="#ddd"/></svg><span class="time">0:16 / 1:05</span></div>
  </div>

  <div class="video v2">
    <div class="vt">VantoMedix</div>
    <div class="frame" role="img" aria-label="Video still: a driver seated in an ambulance cab" style="background:linear-gradient(90deg,#1c1c24 0%,#7d7f96 45%,#c44040 75%,#2a2a30 100%)"></div>
    <div class="play"><svg width="14" height="16"><path d="M0 0l14 8L0 16z" fill="#fff"/></svg></div>
    <div class="track"><i style="width:14%"></i></div>
    <div class="bar"><svg class="ctl" width="40" height="10"><path d="M0 0l8 5-8 5z" fill="#ddd"/><path d="M24 3h3l4-3v10l-4-3h-3z" fill="#ddd"/></svg><span class="time">0:27 / 1:28</span></div>
  </div>

  <div class="video v3">
    <div class="vt">Next Generation Medical Devices Research Th…</div>
    <div class="frame" role="img" aria-label="Video still: title card reading Next Generation Medical Devices" style="background:linear-gradient(135deg,#3a3a3e 0%,#8a8a90 50%,#55555a 100%)"></div>
    <div class="play"><svg width="14" height="16"><path d="M0 0l14 8L0 16z" fill="#fff"/></svg></div>
    <div class="track"><i style="width:6%"></i></div>
    <div class="bar"><svg class="ctl" width="40" height="10"><path d="M0 0l8 5-8 5z" fill="#ddd"/><path d="M24 3h3l4-3v10l-4-3h-3z" fill="#ddd"/></svg><span class="time">0:30 / 6:46</span></div>
  </div>
</section>

<section class="gallery">
  <h2 class="section-title">Gallery</h2>
  <div class="section-sub">Browse through our pictures</div>
  <div class="slide s1" role="img" aria-label="Render of the TubeKeeper fitted to an arm"></div>
  <div class="slide s2" role="img" aria-label="Close-up render of a tube clip on a pale surface"></div>
  <div class="slide s3" role="img" aria-label="Render of the TubeKeeper strap with yellow dial"></div>
  <svg class="arrow prev" width="10" height="16" viewBox="0 0 10 16"><path d="M8 1L2 8l6 7" fill="none" stroke="#fff" stroke-width="2.4"/></svg>
  <svg class="arrow next" width="10" height="16" viewBox="0 0 10 16"><path d="M2 1l6 7-6 7" fill="none" stroke="#fff" stroke-width="2.4"/></svg>
  <div class="dots"><i></i><i></i><i class="on"></i><i class="on"></i><i></i><i></i><i></i><i></i><i></i></div>
</section>

<section class="newsletter">
  <h4>Join our monthly email newsletter</h4>
  <p>We like to keep you up to date with our latest products and news.</p>
  <div class="field f1">Full name</div>
  <div class="field f2">Email ID</div>
  <div class="subscribe">Subscribe</div>
</section>

<footer class="site-footer">
  <div class="copy">Copyright © <a href="#">vantomedix-sample.com</a> 2014. All rights reserved.</div>
  <div class="social"><i></i><i></i><i></i><i></i></div>
</footer>

</body>
</html>
```